Business Card for a Wellness and Aesthetic Center

I'd like to have a business card design for a Wellness and Aesthetic Center based in the Philippines called "Silvermoss Wellness and Aesthetic Inc." They provide services such as medical and aesthetic dermatology. Specializing on cosmetic and anti-aging procedures.

The target market of the business is mostly women from the upper class from 30 to 60 years old.

The feel and look of the card should be feminine, modern, minimalist and classy.

The colors to play with are gold and black.

The front part should contain:
- Name (example: Marisol Teravid Pangilan, MD)
- Designation (example: Medical Director)
- Company Logo

The back part should contain:
- Company Logo
- Address
- Contact Details
- Website

For more details and inspiration you may visit their website at http://silvermossph.com/

Thank you very much!

Target Market(s)

Women from the upper class from 30 to 60 years old.

Industry/Entity Type

Business

Contact Information for Business Card

- Company Logo

- Company Logo
- Address
- Contact Details
- Website

Font styles to use
Serif
Script

Colors
ffc214
fece3e
faa54b
f78f20
000000

Requirements
Must have
• Design should be feminine, modern, minimalist/simple and classy.
Nice to have
• You can play with lines, curves, gardient and be creative on the placement of texts and logo.
Should not have
• Pictures like body, face or nature scene.

```html
<!DOCTYPE html>
<html lang="en">
<head>
<meta charset="UTF-8">
<title>Silvermoss Wellness and Aesthetic Inc. – Business Card</title>
<link rel="stylesheet" href="https://fonts.googleapis.com/css2?family=Montserrat:wght@400;500&family=Open+Sans:wght@400&display=swap">
<style>
  :root {
    --backdrop: #2b2624;
    --card-black: #1c1c1c;
    --card-deep: #121212;
    --gold: #e08a22;
    --gold-soft: #f0a040;
    --text-white: #f4f4f4;
    --text-grey: #9a9a9a;
    --text-dim: #6f6f6f;
  }
  * { margin: 0; padding: 0; box-sizing: border-box; }
  html, body {
    width: 1200px;
    height: 844px;
    overflow: hidden;
    background: var(--backdrop);
  }
  .stage {
    position: relative;
    width: 1200px;
    height: 844px;
  }
  .card {
    position: absolute;
    width: 500px;
    height: 286px;
    overflow: hidden;
    box-shadow: 0 10px 30px rgba(0,0,0,.45);
  }

  /* Contact side */
  .card--contact {
    left: 60px;
    top: 279px;
    background: linear-gradient(120deg, var(--card-black) 55%, #2a2a2a 100%);
  }
  .band {
    position: absolute;
    height: 14px;
    background: var(--gold);
  }
  .band--top { top: 0; left: 0; right: 22px; }
  .band--bottom { bottom: 0; left: 22px; right: 0; }
  .contact-watermark {
    position: absolute;
    left: 50%;
    top: 50%;
    transform: translate(-50%, -50%);
    font-family: "Open Sans", sans-serif;
    font-size: 46px;
    color: #2a2623;
    letter-spacing: 1px;
  }
  .identity {
    position: absolute;
    top: 54px;
    left: 0;
    right: 0;
    text-align: center;
  }
  .identity__name {
    display: inline-block;
    font-family: "Montserrat", sans-serif;
    font-weight: 500;
    font-size: 19px;
    color: var(--text-white);
    letter-spacing: .5px;
    padding-bottom: 4px;
    border-bottom: 1px solid var(--gold);
  }
  .identity__role {
    font-family: "Montserrat", sans-serif;
    font-size: 14px;
    color: var(--text-dim);
    margin-top: 3px;
  }
  .contact-list {
    position: absolute;
    top: 128px;
    left: 0;
    right: 0;
    text-align: center;
    list-style: none;
    font-family: "Open Sans", sans-serif;
    font-size: 14px;
    line-height: 20px;
    color: var(--text-grey);
  }
  .contact-list .address { margin-top: 14px; }

  /* Logo side */
  .card--logo {
    left: 640px;
    top: 279px;
    background: radial-gradient(circle at 50% 45%, #2c2c2c 0%, var(--card-deep) 60%);
  }
  .tab {
    position: absolute;
    width: 24px;
    height: 40px;
    background: var(--gold);
  }
  .tab--right { right: 0; top: 18px; }
  .tab--left { left: 0; top: 150px; }
  .brand {
    position: absolute;
    top: 50%;
    left: 0;
    right: 0;
    transform: translateY(-50%);
    text-align: center;
    font-family: "Open Sans", sans-serif;
    font-size: 36px;
    color: var(--gold-soft);
    letter-spacing: 1px;
  }
</style>
</head>
<body>
<main class="stage">
  <section class="card card--contact">
    <div class="band band--top"></div>
    <div class="band band--bottom"></div>
    <div class="contact-watermark" aria-hidden="true">Silvermoss</div>
    <div class="identity">
      <h1 class="identity__name">JONATHAN SMITH</h1>
      <p class="identity__role">Managing Director</p>
    </div>
    <ul class="contact-list">
      <li>044-456-7890</li>
      <li>123-456-7890</li>
      <li>infoname@yourwebsite.com</li>
      <li>www.website.com</li>
      <li class="address">1234 Address Tag Line | Country Name, AB | 123456</li>
    </ul>
  </section>

  <section class="card card--logo">
    <div class="tab tab--right"></div>
    <div class="tab tab--left"></div>
    <p class="brand">Silvermoss</p>
  </section>
</main>
</body>
</html>
```